Design logo, business cards and letterhead for my eye surgery (doctor's) practice

I am a young eye surgeon (Ophthalmic Surgeon) and I need business cards and letterhead designed ( I have a business card brief and a stationary brief submitted). A small logo would also be useful, or some shape that is seen on both the cards and the letterhead. I am based in Perth, Western Australia. I do some laser refractive work ie LASIK, but also other aspects of ophthalmology as well. The design should be conservative, professional and classic, but also, (as someone who sees young patients for laser surgery) a little interesting to people who refer to me and to patients who will be given my card. The details on the letterhead should be:
Dr Ned Palliser
MBBS (Hons), MMed, FRANZCO
Ophthalmic Surgeon

27 Waverton Ave, Subiaco
Western Australia 6008
Phone: (08) 9217 4602
Facsimile: (08) 9217 4619
Email: reception@nedpalliser.com.au
Provider No: 618095KW

The information on the cards should be the same, but with out the provider number.
On the back of the card should say-

Next Appointment________
The rooms can be accessed easily via public transport, or please feel free to park behind the premises in the designated parking bays.

Target Market(s)

General practitioners and optometrists who refer to me and patients

Industry/Entity Type

Business

Contact Information for Business Card

See above

Requirements
Nice to have
• I've attached a little photo which I thought may make a cute logo of sorts on the cards and letterhead.

```html
<!DOCTYPE html>
<html lang="en">
<head>
<meta charset="utf-8">
<title>Dr Ned Palliser – Business Card</title>
<link rel="stylesheet" href="https://fonts.googleapis.com/css2?family=Orbitron:wght@800&family=Open+Sans:wght@400;600&family=Crimson+Text&display=swap">
<style>
  :root {
    --backdrop: #8f8f8f;
    --card-dark: #2a2a2a;
    --card-light: #e3e3e5;
    --accent-red: #d8202a;
    --text-grey: #4a4a4a;
    --text-dark: #1e1e1e;
    --mark-grey: #8a8a8a;
    --back-text: #e6e6e6;
  }
  * { margin: 0; padding: 0; box-sizing: border-box; }
  html, body { width: 1200px; height: 900px; overflow: hidden; }
  body { background: var(--backdrop); position: relative; font-family: "Open Sans", sans-serif; }

  .card { position: absolute; width: 620px; height: 354px; overflow: hidden; box-shadow: 0 6px 18px rgba(0,0,0,.25); }

  /* Back of card */
  .card-back { left: 530px; top: 80px; background: var(--card-light); }
  .card-back .band { position: absolute; left: 0; right: 0; top: 76px; height: 200px; background: var(--card-dark); padding: 52px 40px 0 36px; color: var(--back-text); font-family: "Crimson Text", serif; font-size: 14px; line-height: 1.35; }
  .card-back .next-appointment { margin-bottom: 14px; }
  .card-back .rule { display: inline-block; width: 200px; border-bottom: 1px solid var(--back-text); margin-left: 4px; }

  /* Front of card */
  .card-front { left: 60px; top: 450px; background: var(--card-light); }
  .card-front .top-band { position: absolute; left: 0; right: 0; top: 0; height: 122px; background: var(--card-dark); }
  .card-front .bottom-band { position: absolute; left: 0; right: 0; bottom: 0; height: 28px; background: var(--card-dark); }
  .practice-mark { position: absolute; left: 48px; top: 44px; display: flex; align-items: center; gap: 12px; }
  .practice-mark .dot { width: 30px; height: 30px; border-radius: 50%; background: var(--accent-red); }
  .practice-mark .mark-name { font-size: 26px; font-weight: 600; color: var(--mark-grey); letter-spacing: 1px; }

  .identity { position: absolute; left: 20px; top: 130px; }
  .doctor-name { font-family: "Orbitron", sans-serif; font-weight: 800; font-size: 19px; color: var(--accent-red); text-transform: uppercase; letter-spacing: .5px; }
  .credentials { font-size: 15px; color: var(--text-grey); line-height: 1.3; margin-top: 2px; }
  .role { font-size: 15px; color: var(--text-grey); padding-left: 36px; }

  .contact-list { position: absolute; right: 22px; top: 186px; list-style: none; text-align: right; }
  .contact-list li { display: flex; justify-content: flex-end; align-items: center; gap: 10px; font-size: 17px; line-height: 27px; color: var(--text-dark); }
  .contact-list svg { width: 14px; height: 14px; fill: var(--text-dark); flex: none; }
</style>
</head>
<body>

<section class="card card-back">
  <div class="band">
    <p class="next-appointment">Next Appointment<span class="rule"></span></p>
    <p class="access-note">The rooms can be accessed easily via public transport, or please feel free to park behind the premises in the designated parking bays.</p>
  </div>
</section>

<section class="card card-front">
  <div class="top-band">
    <div class="practice-mark">
      <span class="dot"></span>
      <span class="mark-name">Palliser Eye</span>
    </div>
  </div>

  <div class="identity">
    <h1 class="doctor-name">Dr Ned Palliser</h1>
    <p class="credentials">MBBS (Hons), MMed, FRANZCO</p>
    <p class="role">Ophthalmic Surgeon</p>
  </div>

  <ul class="contact-list">
    <li>123.456.7890
      <svg viewBox="0 0 16 16"><path d="M1 6c0-2 3-3 7-3s7 1 7 3v1h-4V5.5H5V7H1zM4 8h8l2 6H2z"/></svg></li>
    <li>123.456.7890
      <svg viewBox="0 0 16 16"><path d="M4 1h7v4H4zM2 6h12v9H2zM5 9h2v2H5zm4 0h2v2H9z"/></svg></li>
    <li>info@youremail.com
      <svg viewBox="0 0 16 16"><path d="M1 3h14v10H1zM2 4l6 5 6-5v1L8 10 2 5z" fill-rule="evenodd"/></svg></li>
    <li>www.website.com
      <svg viewBox="0 0 16 16"><path d="M6 10l4-4 1 1-4 4zM3 9l2-2 1 1-2 2a1.5 1.5 0 002 2l2-2 1 1-2 2a3 3 0 01-4-4zm10-2l-2 2-1-1 2-2a1.5 1.5 0 00-2-2L8 6 7 5l2-2a3 3 0 014 4z"/></svg></li>
    <li>1234, Address Goes Here, Country Name, 123456
      <svg viewBox="0 0 16 16"><path d="M8 1a5 5 0 015 5c0 4-5 9-5 9S3 10 3 6a5 5 0 015-5zm0 3a2 2 0 100 4 2 2 0 000-4z" fill-rule="evenodd"/></svg></li>
  </ul>

  <div class="bottom-band"></div>
</section>

</body>
</html>
```